Flyer Design

I need a flyer as Iam starting a business which cleans Leather couches,sofas,chairs for residential and businesses.
We clean the interiors of automobiles and marine craft, boats large and small.
We would like to be able to get across the message that we are affordable, personal and reliable.
The Gold coast is our market and within this area there is a large amount of holiday apartments and houses which do experience high traffic to their living and dinning areas.

Target Market(s)

Target market Home,Apartment,Marine and Auto Owners

Industry/Entity Type

Residential

Requirements
Must have
• The flyer must have Company name which is PURE HIDE RESTORE MOBILE NUMBER
0431759204
EMAIL tramkell@vornexmail.com
Colours would like bright Gold or green or Red eith black lettering very modern font
Nice to have
• I would like to keep it as simple and clean looking.but eye catching
Should not have
• Dont want the flyer to look like a Real Estate flyer or a pizza advertisement.

```html
<!DOCTYPE html>
<html lang="en">
<head>
<meta charset="utf-8">
<title>Pure Hide Restore Flyer</title>
<link rel="stylesheet" href="https://fonts.googleapis.com/css2?family=Archivo+Black&family=Questrial&display=swap">
<style>
  :root {
    --stage: #e9e9e9;
    --paper: #ffffff;
    --oxblood: #8a3a1c;
    --oxblood-dark: #5e2612;
    --gold: #a8893f;
    --gold-light: #b99c55;
    --taupe: #8d7c5e;
    --espresso: #2f2620;
    --ink: #1c1c1c;
    --ink-soft: #444444;
    --light-text: #ffffff;
  }
  * { box-sizing: border-box; margin: 0; padding: 0; }
  html, body { width: 1200px; height: 1000px; overflow: hidden; background: var(--stage); }
  .flyer {
    position: absolute; left: 100px; top: 180px;
    width: 1000px; height: 640px;
    background: var(--paper);
    box-shadow: 0 12px 30px rgba(0,0,0,0.25);
    overflow: hidden;
  }
  .leather-bands { position: absolute; left: 0; top: 0; width: 1000px; height: 490px; }
  .brand { position: absolute; left: 200px; top: 36px; color: var(--light-text); line-height: 0.9; }
  .brand-top { font-family: "Questrial", sans-serif; font-size: 64px; letter-spacing: 1px; display: block; }
  .brand-main { font-family: "Archivo Black", sans-serif; font-size: 92px; display: block; text-shadow: 0 3px 6px rgba(0,0,0,0.35); }
  .tagline {
    position: absolute; left: 200px; top: 240px;
    font-family: "Archivo Black", sans-serif; font-size: 38px;
    color: var(--light-text); text-shadow: 0 2px 4px rgba(0,0,0,0.35);
  }
  .services {
    position: absolute; left: 200px; top: 310px; width: 470px;
    font-family: "Questrial", sans-serif; font-size: 18px; line-height: 1.3;
    color: var(--light-text);
  }
  .contact-strip {
    position: absolute; left: 0; bottom: 0; width: 1000px; height: 150px;
    background: var(--paper);
  }
  .contact-call { position: absolute; left: 60px; top: 28px; color: var(--ink); }
  .contact-lead { font-family: "Questrial", sans-serif; font-size: 28px; display: block; }
  .contact-heading { font-family: "Archivo Black", sans-serif; font-size: 50px; display: block; line-height: 1; }
  .contact-details { position: absolute; left: 560px; top: 30px; list-style: none; }
  .contact-item {
    display: flex; align-items: center; gap: 12px;
    font-family: "Questrial", sans-serif; font-size: 34px; color: var(--ink-soft);
    margin-bottom: 10px;
  }
  .contact-icon { width: 32px; height: 32px; flex: none; }
</style>
</head>
<body>
  <main class="flyer">
    <svg class="leather-bands" viewBox="0 0 1000 490" role="img" aria-label="Diagonal bands of textured leather in oxblood, gold, taupe and dark brown">
      <defs>
        <linearGradient id="goldGrad" x1="0" y1="0" x2="1" y2="1">
          <stop offset="0" stop-color="var(--gold)"/>
          <stop offset="0.5" stop-color="var(--gold-light)"/>
          <stop offset="1" stop-color="var(--gold)"/>
        </linearGradient>
        <linearGradient id="oxGrad" x1="0" y1="0" x2="1" y2="0">
          <stop offset="0" stop-color="var(--oxblood)"/>
          <stop offset="1" stop-color="var(--oxblood-dark)"/>
        </linearGradient>
      </defs>
      <rect width="1000" height="490" fill="url(#goldGrad)"/>
      <polygon points="0,0 560,0 0,300" fill="url(#oxGrad)"/>
      <polygon points="0,0 90,0 0,60" fill="var(--espresso)"/>
      <polygon points="0,490 1000,120 1000,330 420,490" fill="var(--taupe)"/>
      <polygon points="420,490 1000,330 1000,490" fill="var(--espresso)"/>
      <line x1="0" y1="490" x2="1000" y2="120" stroke="#c8b27a" stroke-width="2" opacity="0.6"/>
      <line x1="0" y1="300" x2="560" y2="0" stroke="#c8a060" stroke-width="2" opacity="0.5"/>
    </svg>

    <h1 class="brand">
      <span class="brand-top">PURE HIDE</span>
      <span class="brand-main">RESTORE</span>
    </h1>
    <p class="tagline">Affordable....Personal....Reliable.</p>
    <p class="services">We clean Leather couches,sofas,chairs for residential and businesses. Also We clean the interiors of automobiles and marine craft, boats large and small.</p>

    <section class="contact-strip">
      <div class="contact-call">
        <span class="contact-lead">For More information</span>
        <span class="contact-heading">Contact Us</span>
      </div>
      <ul class="contact-details">
        <li class="contact-item">
          <svg class="contact-icon" viewBox="0 0 32 32" aria-hidden="true">
            <circle cx="16" cy="16" r="14" fill="none" stroke="#333" stroke-width="2.5"/>
            <path d="M12 9 c-2 2 -2 6 1 10 c3 4 6 5 8 4 l1-2 -3-3 -2 1 c-1-1-3-3-3-5 l1-2 -3-3z" fill="#333"/>
          </svg>
          <span>0431759204</span>
        </li>
        <li class="contact-item">
          <svg class="contact-icon" viewBox="0 0 32 32" aria-hidden="true">
            <rect x="2" y="7" width="28" height="18" fill="#333"/>
            <path d="M2 7 L16 18 L30 7" fill="none" stroke="#fff" stroke-width="2"/>
          </svg>
          <span>tramkell@vornexmail.com</span>
        </li>
      </ul>
    </section>
  </main>
</body>
</html>
```